Owen Tasker Studios Business Card

Looking for a clear, modern, elegant, sharp business card that conveys a professional yet edgy image to my business as a wedding, portrait, and travel photographer. Would like something that looks vintage yet modern. Need a new business card to grow my business. We are growing the business for Wedding and Event Photography as well as fine art Photography. (Mostly Landscapes)
Updates

I’m looking through designs now but I have a new logo that i want using please.

New logo uploaded please redesign using that

PLEASE ALL DESIGNERS LOOK IN BRIEF FOR NEW LOGO

Target Market(s)

Brides, Grooms, Families with Kids, People looking for Fine Art Photography Artwork

Industry/Entity Type

Photographer

Contact Information for Business Card

Unsure

Font styles to use
Serif

Colors

Designer to choose colors to be used in the design.

Requirements
Must have
• My Website:
• http://taskerlens.examplefolio.net
• Phone:
• 323-481-5206
• Email:
• owentaskerlens@mailbox-example.net
Nice to have
• Would like a sort of shine on the printing finish.
• I like black I think it looks good on a business card.
• Can try working with my logo (png that I've attached)

```html
<!DOCTYPE html>
<html lang="en">
<head>
<meta charset="utf-8">
<title>Owen Tasker Studios – Business Card</title>
<link href="https://fonts.googleapis.com/css2?family=Josefin+Sans:wght@300;400;600&family=Open+Sans:wght@600;700&display=swap" rel="stylesheet">
<style>
  :root {
    --backdrop: #dcdde1;
    --card-dark: #26262b;
    --card-dark-soft: #34343a;
    --card-light: #ffffff;
    --pattern-grey: #d9d9d9;
    --ink: #1d1d21;
    --icon-grey: #a3a3a8;
  }
  * { margin: 0; padding: 0; box-sizing: border-box; }
  html, body { width: 1200px; height: 960px; overflow: hidden; }
  body { background: var(--backdrop); position: relative; font-family: "Open Sans", sans-serif; }

  .card {
    position: absolute;
    top: 197px;
    width: 327px;
    height: 564px;
    overflow: hidden;
  }

  /* Front */
  .card-front { left: 228px; background: var(--card-dark); }
  .front-texture {
    position: absolute; inset: 0;
    background:
      linear-gradient(180deg, var(--card-dark-soft) 0%, var(--card-dark) 35%, var(--card-dark) 65%, var(--card-dark-soft) 100%);
  }
  .front-brand {
    position: absolute; left: 0; right: 0; top: 222px;
    text-align: center; color: var(--card-light);
  }
  .brand-circle {
    width: 54px; height: 54px; margin: 0 auto 14px;
    border: 3px solid var(--card-light); border-radius: 50%;
  }
  .front-name {
    font-family: "Josefin Sans", sans-serif; font-weight: 600;
    font-size: 27px; letter-spacing: 5px; line-height: 1;
    padding-left: 5px;
  }
  .front-sub {
    margin-top: 12px;
    font-family: "Josefin Sans", sans-serif; font-weight: 600;
    font-size: 9px; letter-spacing: 5px; padding-left: 5px;
  }

  /* Back */
  .card-back { left: 646px; background: var(--card-light); }
  .back-texture {
    position: absolute; left: 0; right: 0; top: 0; height: 200px;
    background: linear-gradient(180deg, var(--pattern-grey) 0%, #efefef 45%, var(--card-light) 100%);
  }
  .back-shape { position: absolute; left: 0; top: 0; }
  .back-name {
    position: absolute; left: 0; right: 0; top: 160px;
    text-align: center; color: var(--ink);
    font-family: "Josefin Sans", sans-serif; font-weight: 300;
    font-size: 27px; letter-spacing: 4px; line-height: 1; padding-left: 4px;
  }
  .back-rule {
    position: absolute; left: 72px; width: 182px; top: 193px;
    height: 2px; background: var(--ink);
  }
  .back-sub {
    position: absolute; left: 0; right: 0; top: 199px;
    text-align: center; color: var(--ink);
    font-family: "Josefin Sans", sans-serif; font-weight: 400;
    font-size: 9px; letter-spacing: 4px; padding-left: 4px;
  }
  .contact-list {
    position: absolute; left: 0; right: 0; top: 294px;
    list-style: none; text-align: center;
  }
  .contact-item {
    display: flex; justify-content: center; align-items: center; gap: 7px;
    height: 29px;
    font-size: 11px; font-weight: 700; color: var(--ink);
  }
  .contact-icon { width: 11px; height: 11px; fill: var(--icon-grey); flex: none; }
</style>
</head>
<body>

<section class="card card-front" aria-label="Card front">
  <div class="front-texture" role="img" aria-label="Subtle dark diamond tile pattern"></div>
  <div class="front-brand">
    <div class="brand-circle"></div>
    <div class="front-name">OWEN TASKER</div>
    <div class="front-sub">STUDIOS</div>
  </div>
</section>

<section class="card card-back" aria-label="Card back">
  <div class="back-texture" role="img" aria-label="Light grey diamond tile pattern"></div>
  <svg class="back-shape" width="327" height="564" viewBox="0 0 327 564" aria-hidden="true">
    <defs>
      <linearGradient id="darkBand" x1="0" y1="0" x2="0" y2="1">
        <stop offset="0" stop-color="#2d2d33"/>
        <stop offset="1" stop-color="#222226"/>
      </linearGradient>
    </defs>
    <polygon points="0,351 164,511 327,351 327,564 0,564" fill="url(#darkBand)"/>
  </svg>

  <div class="back-name">OWEN TASKER</div>
  <div class="back-rule"></div>
  <div class="back-sub">STUDIOS</div>

  <ul class="contact-list">
    <li class="contact-item">
      <svg class="contact-icon" viewBox="0 0 24 24"><path d="M6.6 10.8a15 15 0 0 0 6.6 6.6l2.2-2.2a1 1 0 0 1 1-.25 11.4 11.4 0 0 0 3.6.57 1 1 0 0 1 1 1V20a1 1 0 0 1-1 1A17 17 0 0 1 3 4a1 1 0 0 1 1-1h3.5a1 1 0 0 1 1 1c0 1.25.2 2.45.57 3.57a1 1 0 0 1-.25 1z"/></svg>
      <span>323-481-5206</span>
    </li>
    <li class="contact-item">
      <svg class="contact-icon" viewBox="0 0 24 24"><path d="M2 5h20v14H2z M2 5l10 8 10-8" stroke="#fff" stroke-width="1.5"/></svg>
      <span>owentaskerlens@mailbox-example.net</span>
    </li>
    <li class="contact-item">
      <svg class="contact-icon" viewBox="0 0 24 24"><path d="M3 21 21 3l-5 18-4-8z"/></svg>
      <span>http://taskerlens.examplefolio.net</span>
    </li>
  </ul>
</section>

</body>
</html>
```